Overseas Property Tax Depreciation

We need a two sided flyer to promote our business and explain what we do. our website is www.tolbexmu.net.
The attached word file is what I would like on an A5 size flyer with one side showing the FAQ and the other the worked example. I would like these formatted much better than the are and in general style of the website. I will attach files for logos as well.

```html
<!DOCTYPE html>
<html lang="en">
<head>
<meta charset="utf-8">
<title>Property Tax Depreciation Example</title>
<link rel="stylesheet" href="https://fonts.googleapis.com/css2?family=Open+Sans:wght@400;600;700&display=swap">
<style>
  :root {
    --brand-green: #007236;
    --lime: #a8cf3c;
    --head-pale: #e4eec9;
    --row-light: #d8e8e1;
    --row-dark: #a2c8b1;
    --rule: #ffffff;
    --ink: #1b1b1b;
  }
  * { box-sizing: border-box; margin: 0; padding: 0; }
  html, body { width: 846px; height: 1200px; overflow: hidden; }
  body {
    background: var(--brand-green);
    font-family: "Open Sans", Arial, sans-serif;
    color: var(--ink);
    position: relative;
  }
  .example-sheet {
    position: absolute;
    left: 34px;
    top: 38px;
    width: 778px;
    background: var(--rule);
    border: 2px solid var(--rule);
  }
  .worked-example {
    width: 774px;
    table-layout: fixed;
    border-collapse: collapse;
    font-size: 15px;
    line-height: 1.3;
  }
  .worked-example td, .worked-example th {
    border: 2px solid var(--rule);
    padding: 2px 8px;
    text-align: center;
    vertical-align: middle;
    font-weight: 400;
  }
  .title-band th {
    background: var(--lime);
    font-size: 18.5px;
    font-weight: 600;
    height: 33px;
  }
  .column-head th {
    background: var(--head-pale);
    font-weight: 600;
    font-size: 15.5px;
  }
  .row-light td { background: var(--row-light); }
  .row-dark td { background: var(--row-dark); }
  .label { text-align: left !important; }
  .strong { font-weight: 700 !important; }
  .nowrap { white-space: nowrap; }
  .h30 { height: 29px; }
  .h32 { height: 31px; }
  .h54 { height: 52px; }
  .h76 { height: 74px; }
  .h120 { height: 116px; }
</style>
</head>
<body>
<main class="example-sheet">
  <table class="worked-example">
    <colgroup>
      <col style="width:45px">
      <col style="width:196px">
      <col style="width:119px">
      <col style="width:70px">
      <col style="width:90px">
      <col style="width:86px">
      <col style="width:168px">
    </colgroup>
    <thead>
      <tr class="title-band"><th colspan="7">Property Tax Depreciation Example</th></tr>
      <tr class="title-band"><th colspan="7">3 bed Semi - detached house Dublin, Constructed in 2006</th></tr>
      <tr class="column-head">
        <th rowspan="2">Ref</th>
        <th rowspan="2" colspan="3">Description</th>
        <th colspan="2" class="h54">Without Property Tax Depreciation</th>
        <th class="h54">With Property Depreciation Report</th>
      </tr>
      <tr class="column-head">
        <th class="h32">Euro</th><th>AUD</th><th>AUD</th>
      </tr>
    </thead>
    <tbody>
      <tr class="row-light strong-row">
        <td class="h32 strong">A</td><td class="strong">Rental Income</td><td class="strong">€1,200</td><td class="strong">Month</td><td class="strong">€14,400</td><td class="strong">$20,571</td><td class="strong">$20,571</td>
      </tr>
      <tr class="row-dark">
        <td class="h30"></td><td class="strong">Expenses</td><td></td><td></td><td></td><td></td><td></td>
      </tr>
      <tr class="row-light">
        <td class="h76">B</td><td class="label">Annual Interest charged on outstanding Mortgage (4% apr)</td><td></td><td></td><td>€12,040</td><td>$17,200</td><td>$17,200</td>
      </tr>
      <tr class="row-dark">
        <td class="h54">C</td><td class="label">Property agent fees or commission</td><td></td><td></td><td>€1,200</td><td>$1,714</td><td>$1,714</td>
      </tr>
      <tr class="row-light">
        <td class="h30">D</td><td class="label">Local Property Tax</td><td></td><td></td><td>€250</td><td>$357</td><td>$357</td>
      </tr>
      <tr class="row-dark">
        <td class="h54">E</td><td class="label">Repairs and Maintenance</td><td></td><td></td><td>€2,000</td><td>$2,857</td><td>$2,857</td>
      </tr>
      <tr class="row-light">
        <td class="h32">F</td><td class="label">Home Insurance</td><td></td><td></td><td>€450</td><td>$643</td><td>$643</td>
      </tr>
      <tr class="row-dark">
        <td class="h30">G</td><td class="label">Cleaning Advertising et..</td><td></td><td></td><td>€1,500</td><td>$2,143</td><td>$2,143</td>
      </tr>
      <tr class="row-light">
        <td class="h54 strong">H</td><td class="label strong">Property Tax Depreciation</td><td></td><td></td><td class="strong">€0</td><td class="strong">$0</td><td class="strong">$15,000</td>
      </tr>
      <tr class="row-dark">
        <td class="h32 strong">I</td><td class="label strong">Total Annual Expenses</td><td class="strong nowrap" colspan="2">Total (B to H)</td><td class="strong">€17,440</td><td class="strong">$24,914</td><td class="strong">$39,914</td>
      </tr>
      <tr class="row-light">
        <td class="h54 strong">J</td><td class="label strong">Annual Rental Loss/ Gain</td><td class="strong">(A less I)</td><td></td><td class="strong">-€3,040</td><td class="strong">-$4,343</td><td class="strong">-$19,343</td>
      </tr>
      <tr class="row-dark">
        <td class="h54">K</td><td class="label">Your Annual Income from other sources</td><td></td><td></td><td></td><td>$180,000</td><td>$180,000</td>
      </tr>
      <tr class="row-light">
        <td class="h76">L</td><td class="label">Tour Taxable Income after Rental Losses/ Gains</td><td>(K Plus J)</td><td></td><td></td><td>$175,657</td><td>$160,657</td>
      </tr>
      <tr class="row-dark">
        <td class="h30"></td><td></td><td></td><td></td><td></td><td></td><td></td>
      </tr>
      <tr class="row-light">
        <td class="h76">M</td><td class="label">Your Marginal Income Tax Rate (37% +2% medicare)</td><td></td><td>39%</td><td></td><td></td><td></td>
      </tr>
      <tr class="row-dark">
        <td class="h32">N</td><td class="label">Annual Tax Saving</td><td colspan="2" class="nowrap">(J multiplied by M)</td><td></td><td>$1,694</td><td>$7,544</td>
      </tr>
      <tr class="row-light">
        <td class="h30"></td><td class="label strong">Foreign Tax Credits</td><td></td><td></td><td></td><td></td><td></td>
      </tr>
      <tr class="row-dark">
        <td class="h76">O</td><td class="label">Non-resident Landlord withholding Tax (20% Ireland)</td><td colspan="2" class="nowrap">(A multiplied by 20%)</td><td>€2,880</td><td>$4,114</td><td>$4,114</td>
      </tr>
      <tr class="row-light">
        <td class="h32 strong">P</td><td class="label strong">Nett Tax Savings</td><td class="strong">(N Plus O)</td><td></td><td></td><td class="strong">$5,808</td><td class="strong">$11,658</td>
      </tr>
      <tr class="row-dark">
        <td class="h120 strong">Q</td><td class="label strong">Additional Money in your Pocket (Australia) per year due to Property Tax Depreciation</td><td></td><td></td><td></td><td></td><td class="strong">$5,850</td>
      </tr>
    </tbody>
  </table>
</main>
</body>
</html>
```